Plastic Jar Catalogue 7

We are a plastic factory manufacturing different size of plastic jars, which mostly use for spice and grinded coffee. I need the catalogue to be 3 pages:First page: an attractive cover shows the factory's name and logo with a space for products’ picture. Second page: is an items page which I prefer to be enough for 4 items with a space for item number and description under each item. Last page: to be for factory’s address and contact details.

```html
<!DOCTYPE html>
<html lang="en">
<head>
<meta charset="utf-8">
<title>Clearwell Jar Works – Catalogue</title>
<link href="https://fonts.googleapis.com/css2?family=Montserrat:wght@400;600;700&family=Cinzel:wght@400;500&display=swap" rel="stylesheet">
<style>
  :root{
    --teal:#0093ad;
    --teal-deep:#007f98;
    --green:#8bc34a;
    --white:#ffffff;
    --ink:#1d1d1d;
    --stage:#ececec;
    --jar-light:#f2f2f2;
    --jar-dark:#a9a9a9;
  }
  html,body{margin:0;padding:0;overflow:hidden}
  body{width:1200px;height:1137px;background:var(--stage);position:relative;font-family:'Montserrat',sans-serif}
  .page{position:absolute;width:510px;height:505px;box-shadow:0 2px 6px rgba(0,0,0,.25);overflow:hidden}
  .page--back-cover{left:82px;top:29px;background:var(--white)}
  .page--front-cover{left:602px;top:29px;background:var(--white)}
  .page--items{left:83px;top:562px;background:var(--teal)}
  .page--contact{left:610px;top:564px;background:var(--teal)}

  .cover-art{position:absolute;left:0;top:252px;width:510px;height:253px;background:linear-gradient(180deg,var(--teal) 0%,var(--teal-deep) 45%,var(--green) 100%)}

  .website{position:absolute;left:0;width:510px;top:226px;text-align:center;font-family:'Cinzel',serif;font-size:12px;letter-spacing:1.5px;color:var(--ink)}

  .brand{position:absolute;text-align:center;font-family:'Montserrat',sans-serif;font-weight:600}
  .brand__mark{display:block;letter-spacing:3px}
  .brand__name{display:block;letter-spacing:4px;text-transform:uppercase;line-height:1.45}
  .page--front-cover .brand{left:120px;width:290px;top:114px;color:var(--teal)}
  .page--front-cover .brand__mark{font-size:50px;line-height:1}
  .page--front-cover .brand__name{font-size:14px;margin-top:14px}
  .page--contact .brand{left:55px;width:160px;top:312px;color:var(--white)}
  .page--contact .brand__mark{font-size:30px;line-height:1}
  .page--contact .brand__name{font-size:9px;margin-top:8px;letter-spacing:3px}

  .jar-photo{position:absolute;border-radius:18px 18px 10px 10px;background:linear-gradient(90deg,var(--jar-dark),var(--jar-light) 45%,var(--jar-dark))}
  .page--front-cover .jar-photo{left:210px;top:295px;width:114px;height:168px}

  .item{position:absolute;width:192px;height:230px}
  .item__title{position:absolute;left:0;top:0;margin:0;font-size:10px;font-weight:700;color:var(--white)}
  .item__badge{position:absolute;left:152px;top:-6px;width:45px;height:45px;border-radius:50%;background:var(--green);color:var(--white);font-weight:700;font-size:14px;line-height:45px;text-align:center}
  .item .jar-photo{left:58px;top:17px;width:76px;height:112px}
  .item__text{position:absolute;left:0;top:145px;width:192px;margin:0;font-size:7px;line-height:1.25;color:var(--white);text-align:justify}

  .about__title{position:absolute;left:42px;top:37px;margin:0;font-size:10px;font-weight:700;color:var(--white)}
  .about__col{position:absolute;top:64px;width:193px;font-size:7px;line-height:1.22;color:var(--white);text-align:justify}
  .about__col p{margin:0 0 9px}
  .about__col--left{left:42px}
  .about__col--right{left:262px;width:195px}

  .contact-list{position:absolute;left:276px;top:272px;margin:0;padding:0;list-style:none;font-size:8.5px;color:var(--white)}
  .contact-list li{position:relative;padding-left:30px}
  .contact-list svg{position:absolute;left:0;top:0}
  .contact-list .address{line-height:1.2;height:63px}
  .contact-list .phone{height:26px}
  .contact-list .mail{height:27px}
  .contact-list .social{height:24px}
  .dot{position:absolute;left:3px;top:1px;width:9px;height:9px;border-radius:50%;background:var(--green)}
</style>
</head>
<body>

<section class="page page--back-cover">
  <div class="cover-art" role="img" aria-label="Decorative teal and green wave artwork"></div>
  <div class="website">WWW.WEBSITE.COM</div>
</section>

<section class="page page--front-cover">
  <div class="cover-art" role="img" aria-label="Decorative teal and green wave artwork"></div>
  <div class="brand">
    <span class="brand__mark">CJW</span>
    <span class="brand__name">Clearwell Jar<br>Works</span>
  </div>
  <div class="jar-photo" role="img" aria-label="Product photo: white plastic screw-top jar"></div>
</section>

<section class="page page--items">
  <article class="item" style="left:39px;top:41px">
    <h3 class="item__title">Lorem Ipsum 123</h3>
    <div class="item__badge">123</div>
    <div class="jar-photo" role="img" aria-label="Product photo: white plastic jar with green accent"></div>
    <p class="item__text">Wide-mouth screw-top jar in food-safe plastic, sized for ground spices and coffee. The airtight seal keeps aroma fresh for months. Available in white and clear, with matching lids, custom labels and bulk pricing for packers and roasters of every size. Sample packs on request.</p>
  </article>
  <article class="item" style="left:271px;top:41px">
    <h3 class="item__title">Lorem Ipsum 123</h3>
    <div class="item__badge">123</div>
    <div class="jar-photo" role="img" aria-label="Product photo: white plastic jar with green accent"></div>
    <p class="item__text">Wide-mouth screw-top jar in food-safe plastic, sized for ground spices and coffee. The airtight seal keeps aroma fresh for months. Available in white and clear, with matching lids, custom labels and bulk pricing for packers and roasters of every size. Sample packs on request.</p>
  </article>
  <article class="item" style="left:39px;top:278px">
    <h3 class="item__title">Lorem Ipsum 123</h3>
    <div class="item__badge">123</div>
    <div class="jar-photo" role="img" aria-label="Product photo: white plastic jar with green accent"></div>
    <p class="item__text">Wide-mouth screw-top jar in food-safe plastic, sized for ground spices and coffee. The airtight seal keeps aroma fresh for months. Available in white and clear, with matching lids, custom labels and bulk pricing for packers and roasters of every size. Sample packs on request.</p>
  </article>
  <article class="item" style="left:271px;top:278px">
    <h3 class="item__title">Lorem Ipsum 123</h3>
    <div class="item__badge">123</div>
    <div class="jar-photo" role="img" aria-label="Product photo: white plastic jar with green accent"></div>
    <p class="item__text">Wide-mouth screw-top jar in food-safe plastic, sized for ground spices and coffee. The airtight seal keeps aroma fresh for months. Available in white and clear, with matching lids, custom labels and bulk pricing for packers and roasters of every size. Sample packs on request.</p>
  </article>
</section>

<section class="page page--contact">
  <h2 class="about__title">About Us</h2>
  <div class="about__col about__col--left">
    <p>We mould plastic jars for spice houses, coffee roasters and food packers across the region. Every jar is made from food-grade resin on modern injection lines, checked for wall thickness, thread fit and clarity before it leaves the floor. Our range covers small sample pots to large bulk containers, all with screw lids that seal tight. Custom colours, labels and sizes are available on request, with short lead times and steady supply for growing brands. Our engineers design new moulds in house, so new shapes reach production quickly. Orders ship on pallets or in cartons, packed clean and ready for filling lines, and every batch carries a traceable lot number for your records.</p>
  </div>
  <div class="about__col about__col--right">
    <p>Founded as a family workshop, we now run a full production plant with in-house tooling. Quality control is part of every shift, and our team works closely with clients from sample to delivery. We hold stock of popular sizes for fast dispatch.</p>
    <p>Ask for our full price list and free samples before you place a bulk order. Our sales team replies within one working day.</p>
  </div>

  <div class="brand">
    <span class="brand__mark">CJW</span>
    <span class="brand__name">Clearwell Jar<br>Works</span>
  </div>

  <ul class="contact-list">
    <li class="address">
      <svg width="12" height="16" viewBox="0 0 12 16" aria-hidden="true"><path fill="var(--green)" d="M6,0 C2.7,0 0,2.6 0,5.9 C0,10 6,16 6,16 C6,16 12,10 12,5.9 C12,2.6 9.3,0 6,0Z"/><circle cx="6" cy="6" r="2.2" fill="var(--teal)"/></svg>
      Adress line 1111<br>Adres Line 222<br>Adress Line 3
    </li>
    <li class="phone">
      <svg width="10" height="14" viewBox="0 0 10 14" aria-hidden="true"><rect x="1" y="1" width="8" height="12" rx="1.5" fill="none" stroke="var(--green)" stroke-width="1.6"/><rect x="3" y="3" width="4" height="4" fill="var(--green)"/></svg>
      123 456 789
    </li>
    <li class="mail">
      <svg width="15" height="11" viewBox="0 0 15 11" aria-hidden="true"><rect x="0.8" y="0.8" width="13.4" height="9.4" fill="none" stroke="var(--green)" stroke-width="1.4"/><path d="M1,1 L7.5,6.5 L14,1" fill="none" stroke="var(--green)" stroke-width="1.4"/></svg>
      mail@mail.com
    </li>
    <li class="social"><span class="dot"></span>@CJW</li>
    <li class="social"><span class="dot"></span>@CJW</li>
    <li class="social"><span class="dot"></span>@CJW</li>
  </ul>
</section>

</body>
</html>
```